Lumen Kinetics Web Design Project

We need to update our web design for our company. Lumen Kinetics™ is a series of Development (Training) Programs that we deliver both for the General Public as well as Corporate Business.

Much of the content needs a refresh but we are keen to get some thoughts now on design and layout, predominantly front page. Happy to take any comments on the content if you think that is relevant as well.

We might look to move the current video clip and bring a more generic 'inspirational' clip to the front page. A good example of this is www.mindcraftoz.example.au

Our courses have a very similar market to Gerald Whitcombe type courses ... both General Public and Corporate business.

Refer our website www.lumenkinetics.example.com

Target Market(s)

General Public as well as Corporate Business. Courses are designed for all. Gerald Whitcombe would be a good 'feel' for what we do.

Industry/Entity Type

Business

Requirements
Must have
• Must have a 'leading edge' type feel to it.
Must look professional.

```html
<!DOCTYPE html>
<html lang="en">
<head>
<meta charset="utf-8">
<title>Lumen Kinetics — Home</title>
<link rel="stylesheet" href="https://fonts.googleapis.com/css2?family=Open+Sans:wght@300;400;600;700&family=Signika:wght@400;600&display=swap">
<style>
  :root{
    --brand-blue:#1a6db3;
    --deep-blue:#1360a8;
    --panel-top:#1677cf;
    --panel-bottom:#0aa0ea;
    --nav-top:#6cc6f8;
    --nav-bottom:#2a9be4;
    --nav-active:#17609c;
    --nav-divider:rgba(255,255,255,.35);
    --ink:#5a5a5a;
    --phone-ink:#555;
    --register-red:#ef4a35;
    --register-dark:#a3211a;
    --card-border:#8fb3d6;
    --page-grey:#f1f1f1;
    --white:#fff;
  }
  *{box-sizing:border-box;margin:0;padding:0}
  html,body{width:1200px;height:1000px;overflow:hidden}
  body{position:relative;background:var(--white);font-family:'Open Sans',Arial,sans-serif}
  .top-band{position:absolute;left:0;top:0;width:1200px;height:218px;
    background:var(--page-grey);
    background-image:repeating-linear-gradient(45deg,rgba(0,0,0,.025) 0 1px,transparent 1px 4px)}
  .brand{position:absolute;left:100px;top:22px;display:flex;align-items:flex-start;gap:10px}
  .brand-name{font-family:'Signika',sans-serif;font-weight:400;font-size:40px;line-height:40px;color:var(--brand-blue)}
  .brand-dot{width:16px;height:16px;border-radius:50%;background:var(--brand-blue);margin-top:10px}
  .contact{position:absolute;right:105px;top:42px;font-family:'Signika',sans-serif;font-weight:600;font-size:17px;color:var(--phone-ink)}
  .contact li{list-style:none;display:flex;align-items:center;gap:8px;height:34px;justify-content:flex-end}
  .contact svg{width:14px;height:16px}

  .hero-panel{position:absolute;left:65px;top:178px;width:1060px;height:457px;
    background:radial-gradient(ellipse at 80% 30%,#2aa8ef 0%,transparent 60%),linear-gradient(180deg,var(--panel-top),var(--panel-bottom))}
  .main-nav{position:absolute;left:95px;top:138px;width:1000px;height:80px;display:flex;
    background:linear-gradient(180deg,var(--nav-top),var(--nav-bottom));border-radius:3px 3px 0 0;
    box-shadow:0 2px 4px rgba(0,0,0,.2)}
  .main-nav a{display:flex;align-items:center;justify-content:center;color:var(--white);text-decoration:none;
    font-family:'Signika',sans-serif;font-weight:600;font-size:16px;border-right:1px solid var(--nav-divider);padding-bottom:2px}
  .main-nav a:last-child{border-right:0}
  .main-nav a.is-active{background:linear-gradient(180deg,#2879b8,var(--nav-active))}

  .video{position:absolute;left:96px;top:246px;width:582px;height:329px;border:3px solid var(--white);background:#111;border-radius:2px}
  .video-frame{position:absolute;left:0;top:0;width:576px;height:290px;
    background:radial-gradient(ellipse at 50% 52%,#0a2a9a 0%,#1a4ed8 25%,#2b6bf0 45%,#1a45c4 75%,#0c2a8a 100%)}
  .video-controls{position:absolute;left:0;top:290px;width:576px;height:33px;background:#1b1b1b}
  .progress{position:absolute;left:0;top:290px;width:576px;height:6px;background:#555}
  .progress-played{position:absolute;left:0;top:0;width:18px;height:6px;background:#d22}
  .progress-buffer{position:absolute;left:18px;top:0;width:22px;height:6px;background:#999}
  .progress-knob{position:absolute;left:10px;top:-4px;width:14px;height:14px;border-radius:50%;background:#fff;border:3px solid #d22}
  .time{position:absolute;left:87px;top:303px;font-family:Arial,sans-serif;font-size:11px;color:#fff}
  .time span{color:#aaa}

  .hero-copy{position:absolute;left:720px;top:240px;color:var(--white)}
  .hero-title{font-weight:300;font-size:31px;line-height:36px;text-shadow:0 1px 2px rgba(0,0,0,.2)}
  .hero-title b{font-weight:700}
  .hero-text{margin-top:22px;width:360px;font-size:16px;line-height:24px;text-shadow:0 1px 1px rgba(0,0,0,.2)}
  .register{position:absolute;left:720px;top:478px;width:300px;height:97px}
  .register-label{position:absolute;left:123px;top:22px;color:var(--white);font-weight:600;font-size:16px;line-height:18px}
  .register-label strong{display:block;font-weight:700;font-size:31px;line-height:40px}

  .section-tab{position:absolute;left:100px;top:595px;width:284px;height:40px}
  .section-tab span{position:absolute;left:25px;top:12px;font-family:'Signika',sans-serif;font-weight:600;font-size:19px;color:var(--deep-blue)}

  .carousel-arrow{position:absolute;top:745px;width:26px;height:40px}
  .card{position:absolute;top:664px;width:171px;height:201px;border:1px solid var(--card-border);border-radius:4px;background:var(--white);overflow:hidden;text-align:center}
  .card-photo{height:144px;border-bottom:1px solid var(--card-border)}
  .card-title{margin-top:10px;font-family:Arial,sans-serif;font-weight:700;font-size:15px;color:var(--deep-blue)}
  .card-sub{margin-top:4px;font-family:Arial,sans-serif;font-size:13px;color:#222}
  .card-fold{position:absolute;right:0;top:0;width:16px;height:16px;background:linear-gradient(225deg,var(--white) 50%,#c9d9ea 50%)}

  .divider{position:absolute;left:96px;top:896px;width:999px;height:8px;
    background-image:radial-gradient(#bbb 1px,transparent 1.2px);background-size:3px 3px}
  .intro{position:absolute;left:101px;top:925px;width:600px}
  .intro h2{font-family:'Signika',sans-serif;font-weight:600;font-size:20px;color:var(--deep-blue)}
  .intro p{margin-top:12px;font-family:Arial,sans-serif;font-size:15px;line-height:20px;color:#777}
  .newsletter{position:absolute;left:786px;top:940px;width:301px;height:80px;border:1px solid #ddd;background:linear-gradient(180deg,#fafafa,#f0f0f0);text-align:center}
  .newsletter h3{margin-top:15px;font-family:'Signika',sans-serif;font-weight:600;font-size:19px;color:var(--deep-blue)}
  .newsletter .field{position:absolute;top:53px;width:118px;height:20px;border:1px solid #ccc;border-radius:4px;background:#fff}
</style>
</head>
<body>
  <div class="top-band"></div>

  <header>
    <div class="brand">
      <div class="brand-name">lumen<br>kinetics</div>
      <div class="brand-dot"></div>
    </div>
    <ul class="contact">
      <li>
        <svg viewBox="0 0 14 16"><path d="M3 1l3 3-1.5 2c.8 2 2.2 3.5 4 4.5L10.5 9l3 3-1.5 2.5C6 14 1.5 8 1 2.5z" fill="#1a6db3"/></svg>
        +61 (3) 5550 1428
      </li>
      <li>
        <svg viewBox="0 0 14 16"><rect x="3" y="1" width="8" height="14" rx="1.5" fill="#1a6db3"/><rect x="4.5" y="3" width="5" height="8" fill="#fff"/><circle cx="7" cy="13" r=".9" fill="#fff"/></svg>
        +61 (0) 400 555 917
      </li>
    </ul>
  </header>

  <div class="hero-panel"></div>

  <nav class="main-nav">
    <a href="#" class="is-active" style="width:85px">Home</a>
    <a href="#" style="width:161px">Lumen Kinetics™</a>
    <a href="#" style="width:102px">About Us</a>
    <a href="#" style="width:138px">Our Programs</a>
    <a href="#" style="width:83px">Events</a>
    <a href="#" style="width:131px">Our Products</a>
    <a href="#" style="width:179px">Articles &amp; Resouces</a>
    <a href="#" style="width:121px">Contact Us</a>
  </nav>

  <div class="video">
    <div class="video-frame" role="img" aria-label="Video still of concentric ripples spreading across blue water"></div>
    <div class="video-controls"></div>
    <div class="progress">
      <div class="progress-played"></div>
      <div class="progress-buffer"></div>
      <div class="progress-knob"></div>
    </div>
    <svg style="position:absolute;left:18px;top:303px" width="60" height="16" viewBox="0 0 60 16">
      <rect x="0" y="2" width="4" height="12" fill="#ccc"/><rect x="7" y="2" width="4" height="12" fill="#ccc"/>
      <path d="M38 5h3l4-3v12l-4-3h-3z" fill="#ccc"/><path d="M47 5q2 3 0 6" stroke="#ccc" fill="none" stroke-width="1.5"/>
    </svg>
    <div class="time">0:03 <span>/ 2:41</span></div>
    <svg style="position:absolute;left:404px;top:302px" width="170" height="18" viewBox="0 0 170 18">
      <rect x="2" y="5" width="13" height="8" fill="#bbb"/><rect x="4" y="8" width="9" height="1" fill="#333"/>
      <circle cx="39" cy="9" r="6" fill="#bbb"/><circle cx="39" cy="9" r="2.5" fill="#1b1b1b"/>
      <circle cx="69" cy="9" r="5" fill="#bbb"/>
      <rect x="92" y="5" width="14" height="9" fill="none" stroke="#fff" stroke-width="2"/>
      <rect x="121" y="4" width="16" height="11" fill="none" stroke="#bbb" stroke-width="2"/>
      <path d="M150 3h-3v3M160 3h3v3M150 15h-3v-3M160 15h3v-3" stroke="#bbb" stroke-width="2" fill="none"/>
    </svg>
  </div>

  <section class="hero-copy">
    <h1 class="hero-title">An new way of <b>Thinking</b><br>to <b>create</b> a new way<br>of being</h1>
    <p class="hero-text">Lumen Kinetics™ delivers leading edge work-shops, seminars and products in a fun and interactive way.</p>
  </section>

  <a href="#" class="register">
    <svg width="300" height="97" viewBox="0 0 300 97">
      <polygon points="0,0 104,0 78,97 0,97" fill="var(--register-red)"/>
      <polygon points="104,6 290,6 298,86 78,94" fill="#e8402c"/>
      <polygon points="104,6 290,6 292,30 100,30" fill="#f56a52" opacity=".5"/>
      <circle cx="45" cy="47" r="23" fill="var(--register-dark)"/>
      <polygon points="41,37 53,47 41,57" fill="#fff"/>
    </svg>
    <div class="register-label">CLICK HERE TO<strong>REGISTER</strong></div>
  </a>

  <div class="section-tab">
    <svg width="284" height="40" viewBox="0 0 284 40"><path d="M0 40 L8 6 Q10 0 16 0 H264 L284 40 Z" fill="#fff"/></svg>
    <span>Experience for Yourself</span>
  </div>

  <svg class="carousel-arrow" style="left:70px" viewBox="0 0 26 40"><path d="M22 2 L4 20 L22 38" stroke="var(--deep-blue)" stroke-width="7" fill="none"/></svg>
  <svg class="carousel-arrow" style="left:1096px" viewBox="0 0 26 40"><path d="M4 2 L22 20 L4 38" stroke="var(--deep-blue)" stroke-width="7" fill="none"/></svg>

  <article class="card" style="left:110px">
    <div class="card-photo" role="img" aria-label="Photo of a smiling man with arms spread open under the sky" style="background:linear-gradient(180deg,#e9eef3,#b9cde3)"></div>
    <div class="card-fold"></div>
    <div class="card-title">Lumen Kinetics™</div><div class="card-sub">for You</div>
  </article>
  <article class="card" style="left:310px">
    <div class="card-photo" role="img" aria-label="Photo of a young girl writing at a desk in front of a chalkboard" style="background:linear-gradient(180deg,#3a3a38,#8a6e55)"></div>
    <div class="card-fold"></div>
    <div class="card-title">Lumen Kinetics™</div><div class="card-sub">for Children and Schools</div>
  </article>
  <article class="card" style="left:509px">
    <div class="card-photo" role="img" aria-label="Photo of a businessman in a suit and tie" style="background:linear-gradient(180deg,#f0f0f0,#5a5a5e)"></div>
    <div class="card-fold"></div>
    <div class="card-title">Lumen Kinetics™</div><div class="card-sub">for Business</div>
  </article>
  <article class="card" style="left:709px">
    <div class="card-photo" role="img" aria-label="Photo of a brown and white puppy" style="background:linear-gradient(180deg,#f4f2ef,#c89a6a)"></div>
    <div class="card-fold"></div>
    <div class="card-title">Lumen Kinetics™</div><div class="card-sub">for Animals</div>
  </article>
  <article class="card" style="left:908px">
    <div class="card-photo" role="img" aria-label="Photo of many hands stacked together in a circle" style="background:linear-gradient(135deg,#9bbf6a,#d89a86 50%,#c86a8a)"></div>
    <div class="card-fold"></div>
    <div class="card-title">Lumen Kinetics™</div><div class="card-sub">for Community</div>
  </article>

  <div class="divider"></div>

  <section class="intro">
    <h2>Lumen Kinetics™</h2>
    <p>Lumen Kinetics™ is a leading edge model which introduces a new lens to view yourself and the world you operate within</p>
  </section>

  <aside class="newsletter">
    <h3>Sign Up To Our Newsletter</h3>
    <div class="field" style="left:30px"></div>
    <div class="field" style="left:153px"></div>
  </aside>
</body>
</html>
```